Musician website

I need a website developed for a musician

The style and content of the website were are looking for is like :

https://www.corvallenmusic.example/
https://www.drossgate.example/
https://www.marnelutwick.example/
https://www.olinbrascombe.example/?frontpage=true

The name of the musician is 'Tamsin Orvell'

Attached are some professional photos to use

Number of Pages Required

1 page

```html
<!DOCTYPE html>
<html lang="en">
<head>
<meta charset="utf-8">
<title>Tamsin Orvell</title>
<link href="https://fonts.googleapis.com/css2?family=Oswald:wght@400;500;600&family=Inter:wght@400&display=swap" rel="stylesheet">
<style>
:root{
  --ink:#111111;
  --paper:#ffffff;
  --rule:#222222;
  --footer:#1b1b1b;
  --hero-dark:#1e1f22;
  --hero-mid:#3a3d42;
}
*{margin:0;padding:0;box-sizing:border-box}
html,body{width:1200px;height:3626px;overflow:hidden;background:var(--paper);color:var(--ink);font-family:"Inter",Helvetica,Arial,sans-serif}
.page{position:relative;width:1200px;height:3626px}
.abs{position:absolute}

/* Hero */
.hero{left:0;top:0;width:1200px;height:684px;background:radial-gradient(ellipse at 55% 35%,#4a4c50 0%,var(--hero-mid) 30%,var(--hero-dark) 75%,#141517 100%)}
.brand{left:110px;top:20px;font-family:"Oswald",sans-serif;font-weight:500;font-size:37px;line-height:1;letter-spacing:2px;color:var(--paper)}
.nav{right:112px;top:30px;display:flex;gap:50px;list-style:none}
.nav li{font-family:"Oswald",sans-serif;font-weight:500;font-size:17px;line-height:1;letter-spacing:1px;color:var(--paper)}
.social{left:25px;top:246px;display:flex;flex-direction:column;gap:11px}
.social span{display:flex;align-items:center;justify-content:center;width:40px;height:40px;border-radius:50%;background:var(--paper);
  font-family:"Oswald",sans-serif;font-weight:500;font-size:9px;letter-spacing:.3px;color:var(--ink)}
.hero-title{left:0;top:412px;width:1200px;text-align:center;font-family:"Oswald",sans-serif;font-weight:600;font-size:104px;line-height:1;letter-spacing:1px;
  background:linear-gradient(180deg,#ffffff 0%,#f0f0f0 55%,#9a9a9a 100%);-webkit-background-clip:text;background-clip:text;color:transparent;
  filter:drop-shadow(0 3px 4px rgba(0,0,0,.6))}

/* Section headings */
.kicker{left:0;width:1200px;text-align:center;font-family:"Oswald",sans-serif;font-size:18px;line-height:1;letter-spacing:3px}
.heading{left:0;width:1200px;text-align:center;font-family:"Oswald",sans-serif;font-weight:400;font-size:48px;letter-spacing:.55em;text-indent:.55em;line-height:1}
.heading.long{font-size:38px;letter-spacing:.45em;text-indent:.45em}
.rule{left:573px;width:54px;height:2px;background:var(--rule)}

.about-text{left:170px;width:860px;text-align:center;font-size:16.5px;line-height:33.5px;letter-spacing:-.3px}
.about-text p+p{margin-top:19px}

.strip-title{left:111px;top:1150px;font-family:"Oswald",sans-serif;font-size:19px;line-height:1;letter-spacing:2px}
.strip-sub{left:111px;top:1181px;font-size:16px;line-height:1}
.strip-arrow{left:113px;top:1214px}
.strip{left:111px;top:1260px;display:flex;gap:15px}
.strip .tile{position:relative;width:233px;height:179px}
.play-badge{position:absolute;left:55px;top:69px;display:flex;align-items:center;gap:9px;color:var(--paper);font-family:"Oswald",sans-serif;font-size:15px}
.play-badge i{display:flex;align-items:center;justify-content:center;width:40px;height:40px;border:1.5px solid rgba(255,255,255,.8);border-radius:50%}

.feature-video{left:111px;top:1684px;width:978px;height:509px;background:linear-gradient(120deg,#6e6c68 0%,#8a8884 35%,#b9b7b2 60%,#7d7b78 100%)}
.big-play{position:absolute;left:449px;top:213px;width:84px;height:84px;border-radius:50%;background:rgba(255,255,255,.9);box-shadow:0 0 0 6px rgba(255,255,255,.35);display:flex;align-items:center;justify-content:center}
.video-row{left:111px;top:2223px;display:flex;gap:27px}
.video-row .tile{width:308px;height:249px}

.gram{left:113px;top:2714px;width:975px;height:456px;display:grid;grid-template-columns:repeat(4,1fr);grid-template-rows:repeat(2,1fr)}

.signup{left:279px;top:3418px;width:641px;height:36px;border-bottom:1.5px solid var(--rule);display:flex;justify-content:space-between;align-items:flex-start}
.signup span{font-family:"Oswald",sans-serif;font-size:14px;letter-spacing:1.5px}

.footer{left:0;top:3557px;width:1200px;height:69px;background:var(--footer);color:var(--paper);font-size:14px;display:flex;align-items:center;justify-content:center}
</style>
</head>
<body>
<div class="page">

  <header class="abs hero" role="img" aria-label="Photo of the musician in a denim jacket seated among dark boulders"></header>
  <div class="abs brand">TAMSIN ORVELL</div>
  <ul class="abs nav">
    <li>HOME</li><li>MUSIC</li><li>TOUR</li><li>SHOP</li><li>VIDEOS</li><li>PHOTOS</li>
  </ul>
  <div class="abs social" aria-label="Social links">
    <span>VEXA</span><span>CHIRPA</span><span>NODEL</span><span>LUMI</span>
  </div>
  <h1 class="abs hero-title">TAMSIN ORVELL</h1>

  <!-- About -->
  <div class="abs kicker" style="top:767px">THE STANDARD LOREM</div>
  <h2 class="abs heading" style="top:801px">ABOUT ME</h2>
  <div class="abs rule" style="top:866px"></div>
  <div class="abs about-text" style="top:881px">
    <p>Sed ut perspiciatis unde omnis iste natus error sit voluptatem accusantium doloremque laudantium, totrem aperiam, eaque ipsa quae ab illo inventore veritatis et quasi architecto beatae vitae dicta sunt explicabo. Nemo enim ipsam voluptatem quia voluptas sit aspernatur aut odit aut fugit, sed quia consequuntur magni dolores eos qui ratione voluptatem sequi nesciunt. Neque porro quisquam est, qui dolorem ipsum quia</p>
    <p>Sed ut perspiciatis unde omnis iste natus error sit voluptatem accusantium doloremque laudantium, totrem aperiam, eaque ipsa quae ab illo inventore veritatis et quasi architecto beatae</p>
  </div>

  <div class="abs strip-title">THE STANDARD LOREM</div>
  <div class="abs strip-sub">Natus error sit voluptatem</div>
  <svg class="abs strip-arrow" width="20" height="24" viewBox="0 0 20 24" fill="none" stroke="#111" stroke-width="2"><path d="M10 2v19M3 14l7 7 7-7"/></svg>
  <div class="abs strip">
    <div class="tile" role="img" aria-label="Musician lying on a blue pool table with a guitar" style="background:linear-gradient(160deg,#1c2a4a,#233a6a 60%,#1a2540)"></div>
    <div class="tile" role="img" aria-label="Hands playing a piano keyboard" style="background:linear-gradient(120deg,#d9d9d9,#9a9a9a 55%,#1e1e22)"></div>
    <div class="tile" role="img" aria-label="Musician in a cap standing outdoors" style="background:linear-gradient(160deg,#3d4436,#2a2d2b 60%,#1b1c1e)">
      <div class="play-badge"><i><svg width="12" height="12" viewBox="0 0 12 12"><path d="M2 1l9 5-9 5z" fill="#fff"/></svg></i>PLAY MUSIC</div>
    </div>
    <div class="tile" role="img" aria-label="Silhouette of the musician against a bright window" style="background:radial-gradient(ellipse at 50% 30%,#8a8a8a,#2e2e2e 60%,#111)"></div>
  </div>

  <!-- Videos -->
  <div class="abs kicker" style="top:1542px">THE STANDARD LOREM</div>
  <h2 class="abs heading" style="top:1576px">VIDEOS</h2>
  <div class="abs rule" style="top:1641px"></div>
  <div class="abs feature-video" role="img" aria-label="Video still of the musician playing an acoustic guitar in a living room">
    <div class="big-play"><svg width="22" height="24" viewBox="0 0 22 24"><path d="M3 2l17 10-17 10z" fill="#111"/></svg></div>
  </div>
  <div class="abs video-row">
    <div class="tile" role="img" aria-label="Musician at a black grand piano from above" style="background:linear-gradient(160deg,#d6d3ce,#2a2523 45%,#5a3a26)"></div>
    <div class="tile" role="img" aria-label="Musician with an electric guitar on a white sofa" style="background:linear-gradient(140deg,#ececec,#bdbdbd 40%,#2a2a2e 75%)"></div>
    <div class="tile" role="img" aria-label="Musician reclining with an acoustic guitar" style="background:linear-gradient(140deg,#a6a7a4,#e2e2e0 45%,#2b2b2d 80%)"></div>
  </div>

  <!-- Gallery -->
  <div class="abs kicker" style="top:2583px">FOLLOW ON</div>
  <h2 class="abs heading" style="top:2618px">LUMIGRAM</h2>
  <div class="abs rule" style="top:2683px"></div>
  <div class="abs gram">
    <div role="img" aria-label="Musician with a white guitar by a pool" style="background:linear-gradient(150deg,#6b8a86,#d8d4cc 60%,#3a3a3a)"></div>
    <div role="img" aria-label="Musician seated on garden steps with a guitar" style="background:linear-gradient(160deg,#3e5a34,#5e5a52 60%,#2c2a28)"></div>
    <div role="img" aria-label="Musician seated by a basketball hoop" style="background:linear-gradient(160deg,#9aa0a6,#6a6e72 50%,#1e1f22)"></div>
    <div role="img" aria-label="Musician in a striped shirt" style="background:linear-gradient(150deg,#cfcfcf,#8a8a8a 45%,#1a1a1e)"></div>
    <div role="img" aria-label="Musician dunking a basketball outdoors" style="background:linear-gradient(160deg,#7c8478,#4e5a3e 60%,#2a3020)"></div>
    <div role="img" aria-label="Musician in a denim jacket among foliage" style="background:linear-gradient(160deg,#33402c,#1e2430 60%,#121418)"></div>
    <div role="img" aria-label="Musician lying on a blue pool table" style="background:linear-gradient(160deg,#1c2a4a,#233a6a 60%,#1a2540)"></div>
    <div role="img" aria-label="Musician at a keyboard by a window" style="background:linear-gradient(150deg,#e4e4e4,#9a9a9a 50%,#2a2224)"></div>
  </div>

  <!-- Sign up -->
  <div class="abs kicker" style="top:3273px">THE STANDARD LOREM</div>
  <h2 class="abs heading long" style="top:3317px">SIGN UP TO RECEIVE UPDATES</h2>
  <div class="abs rule" style="top:3371px"></div>
  <div class="abs signup">
    <span>ENTER EMAIL ADDRESS</span>
    <svg width="22" height="20" viewBox="0 0 22 20" aria-label="Send"><path d="M1 10L21 1 15 19 10 12z" fill="#111"/><path d="M10 12L21 1" stroke="#fff" stroke-width="1.2"/></svg>
  </div>

  <footer class="abs footer">Copyright © 2021&nbsp; Tamsin Orvell . All rights reserved.</footer>
</div>
</body>
</html>
```